PEACFUL ACUPUNCTURE PRACTITIONER NEEDS A NEW COAT

I need a new design for an exiting website http://willowgateneedlework.com/ for a acupuncturist. This will be a minimalism design with lots and lots of white space. Home page and one interior page. Please keep the feeling of calm and peaceful serenity. For Color scheme: https://www.morningfernclinic.com/fertility. The bottom part of the home page with sections and links to the service pages: https://harborlotuswellness.com/. The client likes this the best: http://mfclinic.com/. I'm attaching the logo and content pages.

Target Market(s)

Women

Industry/Entity Type

Wellness, health, wellbeing, meditation

Number of Pages Required

2 page

Font styles to use
Sans Serif
Decorative

Colors

Designer to choose colors to be used in the design.

Requirements
Must have
Nice to have
• Follow new website drafts and links
Should not have
• Busy with bright colors. No poping

```html
<!DOCTYPE html>
<html lang="en">
<head>
<meta charset="utf-8">
<title>Willowgate Acupuncture</title>
<link rel="stylesheet" href="https://fonts.googleapis.com/css2?family=Lora:wght@400;700&family=Poppins:wght@300;400&family=Raleway:wght@200;300&display=swap">
<style>
:root{
  --rose:#b9878b;
  --rose-deep:#a8747a;
  --rose-soft:#e9d6d8;
  --rose-veil:rgba(185,135,139,.62);
  --blush:#f5eeee;
  --blush-2:#f0e4e5;
  --ink:#4b4446;
  --ink-soft:#6e6669;
  --line:#d9c6c8;
  --white:#ffffff;
}
*{box-sizing:border-box;margin:0;padding:0}
html,body{width:1200px;height:3142px;overflow:hidden;background:var(--white)}
body{position:relative;font-family:"Poppins",sans-serif;color:var(--ink)}
.abs{position:absolute}

/* header */
.site-header{left:0;top:0;width:1200px;height:75px;background:var(--white);z-index:3}
.main-nav a{position:absolute;top:27px;font-family:"Lora",serif;font-size:16px;color:var(--ink);text-decoration:none}
.main-nav a.active{color:var(--rose)}
.brand-disc{left:472px;top:0;width:256px;height:172px;background:var(--white);border-radius:0 0 128px 128px;z-index:4;text-align:center}
.brand-dot{display:block;width:54px;height:54px;border-radius:50%;background:var(--rose-soft);margin:20px auto 8px}
.brand-name{font-family:"Lora",serif;font-weight:400;font-size:22px;line-height:25px;color:var(--ink)}

/* hero */
.hero{left:0;top:75px;width:1200px;height:674px;background:linear-gradient(100deg,#f1e0e7 0%,#eae4ea 40%,#e8e2e6 60%,#cfc7d6 100%)}
.hero-photo{left:560px;top:75px;width:640px;height:674px;background:radial-gradient(ellipse at 45% 55%,#ece6ea 0%,#ddd4da 45%,rgba(220,210,220,0) 75%)}
.hero-title{left:95px;top:262px;font-family:"Lora",serif;font-weight:700;font-size:61px;line-height:70px;color:var(--rose)}
.hero-sub{left:95px;top:330px;font-family:"Raleway",sans-serif;font-weight:200;font-size:56px;line-height:62px;letter-spacing:1px;color:var(--rose)}
.hero-text{left:95px;top:390px;width:460px;font-size:13.5px;line-height:26px;color:var(--ink);white-space:nowrap}
.btn-ghost{left:94px;top:456px;width:210px;height:44px;border:1.5px solid var(--white);border-radius:22px;background:var(--rose-veil);font-family:"Lora",serif;font-size:15px;color:var(--white);text-align:center;line-height:41px}
.hero-band{left:0;top:712px;width:573px;height:75px;background:var(--rose);color:var(--white);font-family:"Lora",serif;font-size:15px;line-height:75px;padding-left:61px;z-index:2}
.hero-band svg{vertical-align:middle;margin-left:10px}

/* philosophy */
.philosophy{left:0;top:787px;width:1200px;height:786px;background:#fbf8f8}
.section-title{font-family:"Raleway",sans-serif;font-weight:200;font-size:55px;line-height:62px;color:var(--ink)}
.philo-title{left:61px;top:995px}
.rule{height:1.5px;background:var(--rose)}
.philo-rule{left:60px;top:1131px;width:112px}
.philo-text{left:61px;top:1178px;width:420px;font-size:13.5px;line-height:26.3px;color:var(--ink-soft)}
.photo-family{left:793px;top:929px;width:318px;height:373px;background:linear-gradient(160deg,#f3efec 0%,#e8d8cc 50%,#f2ece8 100%)}
.photo-needles{left:607px;top:1215px;width:316px;height:224px;background:linear-gradient(90deg,#f1ece8 0%,#e8c7a8 45%,#dcae8c 100%)}
.v-line{left:590px;top:1485px;width:1px;height:180px;background:var(--line)}

/* services */
.services{left:0;top:1573px;width:1200px;height:586px;background:var(--blush)}
.service{position:absolute;top:1695px;width:247px}
.service-photo{width:247px;height:180px}
.service-label{position:absolute;left:8px;top:153px;width:231px;height:52px;background:var(--white);font-family:"Lora",serif;font-weight:700;font-size:16.5px;color:var(--ink);text-align:center;line-height:52px}
.consult{left:0;top:1942px;width:1200px;text-align:center;font-size:13.5px;line-height:27px;color:var(--ink-soft)}
.call-inline{left:0;top:2012px;width:1200px;text-align:center;font-family:"Lora",serif;font-size:24px;color:var(--rose)}

/* contact */
.contact{left:0;top:2159px;width:1200px;height:607px;background:#fdfbfb}
.contact-photo{left:560px;top:2159px;width:640px;height:607px;background:linear-gradient(90deg,rgba(253,251,251,1) 0%,rgba(242,231,226,.9) 35%,#e6d2c8 70%,#d9c0b2 100%)}
.contact-title{left:0;top:2240px;width:1200px;text-align:center;z-index:2}
.contact-rule{left:545px;top:2316px;width:112px}
.field{position:absolute;height:47px;border:1px solid #cfc7c9;background:rgba(255,255,255,.85);font-size:13.5px;color:var(--ink-soft);padding:13px 12px}
.btn-solid{left:496px;top:2596px;width:210px;height:44px;background:var(--rose);border-radius:22px;color:var(--white);font-family:"Lora",serif;font-size:15px;text-align:center;line-height:44px}
.call-band{left:626px;top:2732px;width:574px;height:73px;background:var(--rose);color:var(--white);font-family:"Lora",serif;font-size:34px;line-height:73px;padding-left:25px;z-index:2}

/* footer */
.site-footer{left:0;top:2766px;width:1200px;height:376px;background:var(--blush-2)}
.footer-brand{left:0;top:2838px;width:1200px;text-align:center}
.footer-nav{left:0;top:2983px;width:1200px;text-align:center}
.footer-nav a{font-family:"Lora",serif;font-size:15px;color:var(--ink);text-decoration:none;margin:0 15px}
.footer-nav a.active{color:var(--rose)}
.footer-info{left:0;top:3019px;width:1200px;text-align:center;font-size:12px;color:var(--ink-soft)}
.footer-copy{left:0;top:3049px;width:1200px;text-align:center;font-size:12px;color:var(--ink-soft)}
.footer-copy span{color:var(--rose)}
.social{left:548px;top:3083px;width:104px;display:flex;justify-content:space-between}
.social span{width:12px;height:12px;border-radius:50%;background:var(--rose)}
</style>
</head>
<body>

<header class="abs site-header">
  <nav class="main-nav">
    <a href="#" class="active" style="left:61px">Home</a>
    <a href="#" style="left:174px">About</a>
    <a href="#" style="left:289px">What We Do</a>
    <a href="#" style="left:817px">Shop</a>
    <a href="#" style="left:922px">Testimonials</a>
    <a href="#" style="left:1082px">Contact</a>
  </nav>
</header>
<div class="abs brand-disc">
  <span class="brand-dot"></span>
  <div class="brand-name">Willowgate<br>Acupuncture</div>
</div>

<section class="abs hero" role="img" aria-label="Soft-focus photo of a pregnant woman in a white dress holding her belly"></section>
<div class="abs hero-photo"></div>
<h1 class="abs hero-title">Willowgate Point</h1>
<div class="abs hero-sub">ACUPUNCTURE</div>
<p class="abs hero-text">Harmonize physical, mental and emotional wellbeing to<br>strengthen the Willowgate Point from which we all strive to live</p>
<div class="abs btn-ghost">Get An Appointment</div>
<div class="abs hero-band">Philosophy of Care Acupuncture &amp; Chinese Herbal Medicine
  <svg width="24" height="12" viewBox="0 0 24 12"><path d="M0 6h22M17 1l5 5-5 5" fill="none" stroke="#fff" stroke-width="1.4"/></svg>
</div>

<section class="abs philosophy"></section>
<h2 class="abs section-title philo-title">Philosophy of<br>Care</h2>
<div class="abs rule philo-rule"></div>
<p class="abs philo-text">Acupuncture &amp; Chinese Herbal Medicine are rooted in over 3000 years of history and tradition. As a complete medical system that has remained flexible and relevant we honor what has worked from the past while embracing the medicine of tomorrow.</p>
<div class="abs photo-family" role="img" aria-label="Photo of a smiling mother and baby under a white blanket"></div>
<div class="abs photo-needles" role="img" aria-label="Photo of acupuncture needles placed on a back"></div>
<div class="abs v-line"></div>

<section class="abs services"></section>
<div class="service" style="left:60px">
  <div class="service-photo" role="img" aria-label="Photo of baby birds in a nest" style="background:linear-gradient(160deg,#d9d68a,#9aa44c 55%,#6f7a36)"></div>
  <div class="service-label">fertility &amp; pregnancy</div>
</div>
<div class="service" style="left:338px">
  <div class="service-photo" role="img" aria-label="Photo of hands holding a red heart" style="background:linear-gradient(160deg,#c8b2ad,#c78a80 50%,#a66a63)"></div>
  <div class="service-label">Emotional well being</div>
</div>
<div class="service" style="left:615px">
  <div class="service-photo" role="img" aria-label="Photo of stacked stones on raked sand" style="background:linear-gradient(180deg,#ecebe8,#d9d6d0 60%,#c9c4bc)"></div>
  <div class="service-label">Hormone balance</div>
</div>
<div class="service" style="left:893px">
  <div class="service-photo" role="img" aria-label="Photo of a large tree with sunlight in a forest" style="background:linear-gradient(170deg,#4f5a33,#8b8f5a 50%,#a0734a)"></div>
  <div class="service-label">Strength &amp; structure</div>
</div>
<p class="abs consult">Consultations are always available to help answer any questions you may have about<br>acupuncture or herbal medicine in a relaxed environment.</p>
<div class="abs call-inline">Call Us On : 413-555-0182</div>

<section class="abs contact"></section>
<div class="abs contact-photo" role="img" aria-label="Photo of a smiling pregnant woman sitting by a bright window"></div>
<h2 class="abs section-title contact-title">Get In Touch With Us</h2>
<div class="abs rule contact-rule"></div>
<div class="field" style="left:291px;top:2362px;width:302px">Name</div>
<div class="field" style="left:606px;top:2362px;width:302px">Contact No.</div>
<div class="field" style="left:291px;top:2422px;width:617px">Email</div>
<div class="field" style="left:291px;top:2482px;width:617px;height:99px">Message</div>
<div class="abs btn-solid">Get An Appointment</div>
<div class="abs call-band">Call Us On : 413-555-0182</div>

<footer class="abs site-footer"></footer>
<div class="abs footer-brand">
  <span class="brand-dot" style="margin:0 auto 10px"></span>
  <div class="brand-name" style="font-size:24px;line-height:27px">Willowgate<br>Acupuncture</div>
</div>
<nav class="abs footer-nav">
  <a href="#" class="active">Home</a><a href="#">About</a><a href="#">What We Do</a><a href="#">Shop</a><a href="#">Testimonials</a><a href="#">Contact</a>
</nav>
<p class="abs footer-info">48 Alder Row, Easthaven, MA 01099 &nbsp;|&nbsp; info@willowgateneedlework.com</p>
<p class="abs footer-copy">© <span>Willowgate Acupuncture</span> - 2021. All Rights Reserved.</p>
<div class="abs social"><span></span><span></span><span></span><span></span></div>

</body>
</html>
```